Alderbrook Church Bulletin Design

We need a refreshed bulletin design for our church. We are looking to use a the same blue we use in our new logo and a clean and simple design. Our current design is very dated (created and maintained in Microsoft Publisher) and too busy/crowded. There are too many font styles. It needs to be simplified and updated. I am happy to elaborate more if needed.

Industry/Entity Type

Religious

Font styles to use
Sans Serif

Colors
0792cd
33a6d7
85cae6
0255a3
3176b5
85acd3

Requirements
Must have
• See ideas submitted

```html
<!DOCTYPE html>
<html lang="en">
<head>
<meta charset="utf-8">
<title>Alderbrook Church Bulletin – Pages 9–10</title>
<link href="https://fonts.googleapis.com/css2?family=Lato:wght@400;700&display=swap" rel="stylesheet">
<style>
  :root {
    --blue-bright: #0792cd;
    --blue-sky: #33a6d7;
    --blue-pale: #85cae6;
    --blue-deep: #0255a3;
    --blue-mid: #3176b5;
    --blue-dusty: #85acd3;
    --ink: #6a6a6a;
    --title-blue: #3a9bd5;
    --white: #ffffff;
  }
  * { margin: 0; padding: 0; box-sizing: border-box; }
  html, body { width: 1200px; height: 726px; overflow: hidden; background: var(--white); }
  .spread {
    position: relative;
    width: 1200px;
    height: 726px;
    overflow: hidden;
    font-family: "Lato", sans-serif;
    background: var(--white);
  }
  .backdrop { position: absolute; inset: 0; display: block; }
  .hymn {
    position: absolute;
    left: 140px; top: 43px; width: 320px;
    text-align: center;
    color: var(--ink);
    font-weight: 700;
    font-size: 11px;
    line-height: 11.2px;
  }
  .hymn__credit {
    margin-top: 5px;
    font-weight: 400;
    font-size: 9.4px;
    line-height: 11px;
  }
  .dismissal {
    position: absolute;
    left: 624px; top: 72px; width: 280px;
    text-align: center;
    color: var(--ink);
  }
  .dismissal__title {
    color: var(--title-blue);
    font-weight: 700;
    font-size: 13px;
    line-height: 16px;
    margin-bottom: 3px;
  }
  .dismissal__body {
    font-weight: 700;
    font-size: 11px;
    line-height: 11.2px;
  }
  .prayer {
    position: absolute;
    left: 42px; top: 442px; width: 200px;
    text-align: center;
    color: var(--white);
  }
  .prayer__title {
    font-weight: 700;
    font-size: 12.8px;
    line-height: 16px;
    margin-bottom: 1px;
  }
  .prayer__body {
    font-weight: 700;
    font-size: 9.8px;
    line-height: 11.2px;
  }
  .prayer__body + .prayer__body { margin-top: 5px; }
  .leader-portrait {
    position: absolute;
    left: 91px; top: 329px;
    width: 102px; height: 102px;
    border-radius: 50%;
    border: 3px solid var(--white);
    background: radial-gradient(circle at 50% 45%, #b98a6e 0%, #8a6652 40%, #c9c4bd 75%);
  }
  .page-number {
    position: absolute;
    top: 700px;
    font-weight: 700;
    font-size: 15px;
    line-height: 18px;
  }
  .page-number--left { left: 28px; color: var(--blue-bright); }
  .page-number--right { left: 1158px; color: var(--white); }
</style>
</head>
<body>
<main class="spread">
  <svg class="backdrop" width="1200" height="726" viewBox="0 0 1500 908" preserveAspectRatio="none">
    <defs>
      <linearGradient id="artworkTone" x1="0" y1="1" x2="1" y2="0">
        <stop offset="0" stop-color="var(--blue-deep)"/>
        <stop offset="0.3" stop-color="var(--blue-deep)"/>
        <stop offset="0.55" stop-color="var(--blue-mid)"/>
        <stop offset="0.75" stop-color="var(--blue-bright)"/>
        <stop offset="1" stop-color="var(--blue-sky)"/>
      </linearGradient>
      <linearGradient id="familyPhotoTone" x1="0" y1="0" x2="1" y2="1">
        <stop offset="0" stop-color="#b9c9a0"/>
        <stop offset="0.4" stop-color="#8fa3b8"/>
        <stop offset="0.75" stop-color="#6f86a6"/>
        <stop offset="1" stop-color="#9fb07a"/>
      </linearGradient>
    </defs>
    <g role="img" aria-label="Decorative blue geometric artwork framing the page">
      <polygon points="0,310 498,632 1045,363 1180,110 1105,0 1500,0 1500,908 0,908" fill="url(#artworkTone)"/>
    </g>
    <g role="img" aria-label="Photo of a smiling family of four sitting together on the grass outdoors">
      <polygon points="960,535 1500,275 1500,908 990,908" fill="url(#familyPhotoTone)"/>
    </g>
  </svg>

  <section class="hymn">
    <p>Jesus, Master, Whose I Am</p>
    <p>Jesus, Master, whose I am,<br>Purchased thine alone to be<br>By thy blood, O spotless Lamb,<br>Shed so willingly for me,<br>Let my heart be all thine own,<br>Let me live to thee alone.<br>Jesus, Master, I am thine:<br>Keep me faithful, keep me near;<br>Let thy presence in me shine<br>All my homeward way to cheer.<br>Jesus, at thy feet I fall,<br>O be thou my all in all.<br>Jesus, Master, whom I serve,<br>Though so feebly and so ill,<br>Strengthen hand and heart and nerve<br>All thy bidding to fulfil.<br>Open thou mine eyes to see<br>All the work thou hast for me.<br>Lord, thou needest not, I know,<br>Service such as I can bring;<br>Yet I long to prove and show<br>Full allegiance to my King.<br>Thou an honor art to me:<br>Let me be a praise to thee.</p>
    <p class="hymn__credit">© 2017 Frances R. Holloway/Stewart Mills<br>SRL License No. 4827150</p>
  </section>

  <section class="dismissal">
    <h2 class="dismissal__title">Jr. Church Dismissal</h2>
    <p class="dismissal__body">At this time children 4-6 years old may<br>be dismissed to Junior Church, which<br>meets in the Junior Church room.<br>Younger children also may be escorted<br>to their appropriate classrooms at this<br>time. Children who attend junior church<br>will return to the sanctuary following<br>the closing of the sermon.<br>Of course, children of all<br>ages are welcome to remain<br>in the sanctuary for the</p>
  </section>

  <div class="leader-portrait" role="img" aria-label="Portrait photo of the prayer leader"></div>

  <section class="prayer">
    <h2 class="prayer__title">Corporate Prayer</h2>
    <p class="prayer__body">Lorem ipsum dolor sit amet,<br>consectetur adipiscing elit, sed do<br>eiusmod tempor incididunt ut</p>
    <p class="prayer__body">labore et dolore magna aliqua. Ut<br>enim ad minim veniam, quis nostrud<br>exercita on ullamco.</p>
  </section>

  <span class="page-number page-number--left">9</span>
  <span class="page-number page-number--right">10</span>
</main>
</body>
</html>
```